Fernhollow Estates Cards and Letterhead
EPS and PNG formatted logo files have been uploaded
Please feel free to post ideas for letterhead / stationary as well. Thanks.
SiteAdmin - I haven't yet received my logo files. If there is somewhere I can download them from please let me know. Thanks.
Attention Project Holder!!
Please be advised to upload your logo file in AI, EPS or PNG format so that the designers can incorporate your logo in this designs.
QT/PWF/HR Team
If you have the ability to create a couple of PowerPoint master slides based on the look and feel of the logo I'd be willing to pay extra for those. Thx.

```html
<!DOCTYPE html>
<html lang="en">
<head>
<meta charset="utf-8">
<title>Fernhollow Estates – Business Card</title>
<link rel="stylesheet" href="https://fonts.googleapis.com/css2?family=Roboto:ital,wght@0,400;0,700;1,400&display=swap">
<style>
  :root {
    --navy: #1f3a78;
    --navy-deep: #14295c;
    --navy-light: #3a5aa0;
    --green: #3f9a3c;
    --white: #ffffff;
    --grey-text: #4a4f5c;
    --backdrop: #e6e7ea;
  }
  * { box-sizing: border-box; margin: 0; padding: 0; }
  html, body {
    width: 1200px; height: 871px; overflow: hidden;
    background: var(--backdrop);
    font-family: "Roboto", Arial, sans-serif;
  }
  .stage { position: relative; width: 1200px; height: 871px; }
  .card {
    position: absolute; left: 250px; width: 700px; height: 400px;
    overflow: hidden; border-radius: 4px;
    box-shadow: 0 6px 18px rgba(0,0,0,0.18);
  }
  .card--back { top: 24px; background: linear-gradient(160deg, var(--navy-light), var(--navy-deep)); }
  .card--front { top: 447px; background: var(--white); }

  .back-mark {
    position: absolute; left: 0; right: 0; top: 150px;
    display: flex; align-items: center; justify-content: center; gap: 16px;
    color: var(--white); font-weight: 700; font-size: 40px; letter-spacing: 2px; text-transform: uppercase;
  }
  .back-mark .mark-square { width: 34px; height: 34px; background: var(--white); opacity: 0.85; }
  .back-web {
    position: absolute; left: 0; right: 0; top: 300px; text-align: center;
    color: rgba(255,255,255,0.75); font-size: 13px; letter-spacing: 1px;
  }

  .brand {
    position: absolute; left: 40px; top: 48px;
    display: flex; align-items: center; gap: 10px;
    color: var(--navy); font-weight: 700; font-size: 25px; letter-spacing: 1px; text-transform: uppercase;
  }
  .brand .mark-square { width: 22px; height: 22px; background: var(--navy); }
  .brand-rule { position: absolute; left: 40px; top: 90px; width: 300px; height: 3px; background: var(--green); }

  .person { position: absolute; right: 40px; top: 128px; text-align: right; }
  .person-name { color: var(--navy); font-weight: 700; font-size: 19px; }
  .person-title { color: var(--grey-text); font-style: italic; font-size: 13px; margin-top: 4px; }

  .lower-band {
    position: absolute; left: 0; right: 0; top: 236px; bottom: 0;
    background: linear-gradient(180deg, var(--navy-light) 0%, var(--navy) 35%, var(--navy-deep) 100%);
    border-top: 6px solid var(--green);
  }

  .contact { position: absolute; right: 40px; top: 258px; text-align: right; color: var(--white); font-size: 12.5px; line-height: 17px; }
  .contact-address { margin-bottom: 8px; }
  .contact-line { display: flex; justify-content: flex-end; align-items: center; gap: 10px; }
  .contact-line svg, .email svg { width: 12px; height: 12px; flex: none; }
  .email {
    position: absolute; right: 40px; top: 364px;
    display: flex; align-items: center; gap: 10px;
    color: var(--white); font-size: 12.5px;
  }
</style>
</head>
<body>
<main class="stage">
  <section class="card card--back" aria-label="Card back">
    <div class="back-mark"><span class="mark-square"></span>Fernhollow Estates</div>
    <div class="back-web">www.fernhollowestates.com</div>
  </section>

  <section class="card card--front" aria-label="Card front">
    <div class="lower-band" role="img" aria-label="Decorative navy and green wave band"></div>

    <div class="brand"><span class="mark-square"></span>Fernhollow Estates</div>
    <div class="brand-rule"></div>

    <div class="person">
      <div class="person-name">Dana Whitcombe</div>
      <div class="person-title">Your Job Title</div>
    </div>

    <div class="contact">
      <div class="contact-address">Unit 48 Larch Avenue,<br>Westbury 5521 Country</div>
      <div class="contact-line">201 555 0143
        <svg viewBox="0 0 12 12" aria-hidden="true"><path d="M2 1h3l1 3-2 1a7 7 0 0 0 3 3l1-2 3 1v3c-6 0-10-4-10-9z" fill="var(--white)"/></svg></div>
      <div class="contact-line">201 555 0178
        <svg viewBox="0 0 12 12" aria-hidden="true"><rect x="3" y="0.5" width="6" height="11" rx="1" fill="none" stroke="var(--white)"/><circle cx="6" cy="9.5" r="0.8" fill="var(--white)"/></svg></div>
      <div class="contact-line">201 555 0190
        <svg viewBox="0 0 12 12" aria-hidden="true"><rect x="1" y="4" width="10" height="6" fill="none" stroke="var(--white)"/><rect x="3" y="1" width="6" height="3" fill="none" stroke="var(--white)"/></svg></div>
    </div>
    <div class="email">dana.whitcombe@fernhollowestates.com
      <svg viewBox="0 0 12 12" aria-hidden="true"><rect x="0.5" y="2.5" width="11" height="7" fill="none" stroke="var(--white)"/><path d="M0.5 2.5l5.5 4 5.5-4" fill="none" stroke="var(--white)"/></svg></div>
  </section>
</main>
</body>
</html>
```